Ashcombe Field Surveyors Business Card

We are a land surveying company looking for a business card with a clean, sharp design. We would like for our design to portray our logo on one side, and contact information on the other w/ or w/o logo. Our colors preferred are navy blue, grey/silver, white and black. thank you!

Industry/Entity Type

Surveyor

Contact Information for Business Card

Ashcombe Field Surveyors
Dorian Kavatsky, P.L.S.
(555) 302-4619
Ashcombefieldsurveyors@ashmail-example.net
Ashcombefieldsurveyors-example.com
287 Linden Terrace, Brookhollow MA 01999

Requirements
Must have
• 1. Company Name
2. Personal name and title
3. phone number
4. email.
5. website
6. address

```html
<!DOCTYPE html>
<html lang="en">
<head>
<meta charset="utf-8">
<title>Ashcombe Field Surveyors – Business Card</title>
<link href="https://fonts.googleapis.com/css2?family=Lato:wght@400;700;900&display=swap" rel="stylesheet">
<style>
  :root {
    --navy: #2e3192;
    --navy-line: #3a3d9c;
    --white: #ffffff;
    --ink: #4a4a52;
    --bg: #d2d3cf;
  }
  * { box-sizing: border-box; margin: 0; padding: 0; }
  html, body { width: 1200px; height: 801px; overflow: hidden; }
  body {
    background: var(--bg);
    font-family: 'Lato', sans-serif;
    display: flex;
    align-items: center;
    justify-content: center;
    gap: 50px;
  }
  .card {
    width: 525px;
    height: 300px;
    position: relative;
    box-shadow: 0 10px 24px rgba(0,0,0,0.22);
    overflow: hidden;
  }

  /* Contact side */
  .card--front { background: var(--white); }
  .front__brand {
    position: absolute;
    left: 36px;
    top: 110px;
    width: 195px;
    display: flex;
    align-items: center;
    gap: 12px;
  }
  .brand__dot {
    flex: none;
    width: 30px; height: 30px;
    border-radius: 50%;
    background: var(--navy);
  }
  .brand__name {
    color: var(--navy);
    font-weight: 900;
    font-size: 20px;
    line-height: 1.1;
    text-transform: uppercase;
    letter-spacing: 1px;
  }
  .front__divider {
    position: absolute;
    left: 244px;
    top: 108px;
    width: 1px;
    height: 96px;
    background: var(--navy-line);
  }
  .front__person {
    position: absolute;
    left: 262px;
    top: 40px;
  }
  .person__name {
    color: var(--navy);
    font-weight: 900;
    font-size: 21px;
    letter-spacing: -0.2px;
  }
  .person__title {
    color: var(--ink);
    font-size: 12.5px;
    margin-top: 2px;
  }
  .front__contacts {
    position: absolute;
    left: 262px;
    top: 118px;
    list-style: none;
  }
  .contact {
    display: flex;
    align-items: center;
    gap: 9px;
    color: var(--ink);
    font-size: 10.5px;
    height: 22px;
    white-space: nowrap;
  }
  .contact svg { width: 12px; height: 12px; flex: none; }
  .front__band {
    position: absolute;
    left: 0; right: 0;
    top: 228px;
    height: 36px;
    background: var(--navy);
    display: flex;
    align-items: center;
    justify-content: center;
  }
  .band__address {
    color: var(--white);
    font-size: 14px;
    letter-spacing: 0.3px;
  }

  /* Brand side */
  .card--back {
    background: var(--navy);
    display: flex;
    align-items: center;
    justify-content: center;
    gap: 16px;
  }
  .back__dot {
    width: 44px; height: 44px;
    border-radius: 50%;
    background: var(--white);
  }
  .back__name {
    color: var(--white);
    font-weight: 900;
    font-size: 30px;
    line-height: 1.08;
    text-transform: uppercase;
    letter-spacing: 2px;
  }
</style>
</head>
<body>
  <section class="card card--front" aria-label="Business card, contact side">
    <div class="front__brand">
      <span class="brand__dot"></span>
      <span class="brand__name">Ashcombe Field Surveyors</span>
    </div>
    <div class="front__divider"></div>
    <div class="front__person">
      <p class="person__name">Dorian Kavatsky, P.L.S.</p>
      <p class="person__title">Founder &amp; CEO</p>
    </div>
    <ul class="front__contacts">
      <li class="contact">
        <svg viewBox="0 0 24 24" aria-hidden="true"><path fill="#2e3192" d="M6.6 10.8a15.1 15.1 0 0 0 6.6 6.6l2.2-2.2a1 1 0 0 1 1-.25 11.4 11.4 0 0 0 3.6.57 1 1 0 0 1 1 1V20a1 1 0 0 1-1 1A17 17 0 0 1 3 4a1 1 0 0 1 1-1h3.5a1 1 0 0 1 1 1c0 1.25.2 2.45.57 3.57a1 1 0 0 1-.25 1z"/></svg>
        (555) 302-4619
      </li>
      <li class="contact">
        <svg viewBox="0 0 24 24" aria-hidden="true"><rect x="2" y="5" width="20" height="14" fill="#2e3192"/><path d="M2 5l10 8 10-8" fill="none" stroke="#fff" stroke-width="2"/></svg>
        Ashcombefieldsurveyors@ashmail-example.net
      </li>
      <li class="contact">
        <svg viewBox="0 0 24 24" aria-hidden="true"><circle cx="12" cy="12" r="10" fill="#2e3192"/><path d="M2 12h20M12 2c3 3 3 17 0 20M12 2c-3 3-3 17 0 20" fill="none" stroke="#fff" stroke-width="1.3"/></svg>
        www.Ashcombefieldsurveyors-example.com
      </li>
    </ul>
    <div class="front__band">
      <p class="band__address">287 Linden Terrace, Brookhollow MA 01999</p>
    </div>
  </section>

  <section class="card card--back" aria-label="Business card, brand side">
    <span class="back__dot"></span>
    <span class="back__name">Ashcombe<br>Field Surveyors</span>
  </section>
</body>
</html>
```